Business Cards and Logo

KMR - Personal Injury Attorneys is the name of the firm.
We are personal injury lawyers. We want a crisp, modern and impactful design.
Color schemes are white, matte black and light grey OR white, matte black and red OR white, matte black and a nice blue or yellow.
For logo - we don’t want typical logos like scales of justice or a hammer. We want a general design with the KMR letters.
Target Market(s)
People who need attorneys.
Industry/Entity Type
Law Firm
Contact Information for Business Card
Back side: text: Los Angeles - Santa Ana - San Diego - San Francisco
Front side
Name of firm and logo.
Tomas Velquist
712 W. Harlow Ave. 4th Floor
Brookvale, CA 90000
(555)014-2736 (c)
(555)019-6521 (o)
Tomas@counselwestex.com
Logo Text
KMR
Font styles to use
Other font styles liked:
- Musk - regular. Military - regular. Moonglade. Future. Or similar fonts.
Requirements
Must have
- See above. Nothing else to provide.
- KMR - Personal Injury Attorneys is the name of the firm.
- We are personal injury lawyers. We want a crisp, modern and impactful design.
- Color schemes are white, matte black and light grey OR white, matte black and red OR white, matte black and a nice blue or yellow.
- For logo - we don’t want typical logos like scales of justice or a hammer. We want a general design with the KMR letters.
Nice to have
- See above - nothing else to provide.
Should not have

```html
<!DOCTYPE html>
<html lang="en">
<head>
<meta charset="utf-8">
<title>KMR - Personal Injury Attorneys · Business Card</title>
<link rel="stylesheet" href="https://fonts.googleapis.com/css2?family=Bitter:wght@400;700&family=Arimo:wght@400&display=swap">
<style>
  :root {
    --matte-black: #0b0b0b;
    --paper-white: #ffffff;
    --stage-grey: #e4e4e4;
    --ink: #111111;
    --soft-ink: #333333;
  }
  * { box-sizing: border-box; margin: 0; padding: 0; }
  html, body { width: 1200px; height: 900px; overflow: hidden; }
  body {
    background: var(--stage-grey);
    position: relative;
    font-family: "Arimo", Arial, sans-serif;
  }
  .card {
    position: absolute;
    left: 320px;
    width: 560px;
    height: 320px;
    overflow: hidden;
    box-shadow: 0 6px 18px rgba(0,0,0,0.18);
  }
  .card--front { top: 95px; background: var(--paper-white); }
  .card--back { top: 485px; background: var(--matte-black); }

  /* Front side */
  .front-band {
    height: 118px;
    background: var(--matte-black);
    display: flex;
    align-items: center;
    justify-content: center;
  }
  .firm-name {
    font-family: "Bitter", Georgia, serif;
    font-weight: 700;
    color: var(--paper-white);
    text-align: center;
    line-height: 1;
  }
  .firm-name__letters { display: block; font-size: 58px; letter-spacing: 2px; }
  .firm-name__tagline { display: block; font-size: 13px; margin-top: 6px; letter-spacing: 0.5px; }

  .front-details {
    text-align: center;
    color: var(--ink);
    padding-top: 12px;
  }
  .person-name {
    font-family: "Bitter", Georgia, serif;
    font-weight: 700;
    font-size: 19px;
  }
  .person-title {
    font-family: "Bitter", Georgia, serif;
    font-size: 11px;
    color: var(--soft-ink);
    margin-bottom: 10px;
  }
  .detail-label {
    font-family: "Bitter", Georgia, serif;
    font-weight: 700;
    font-size: 12px;
    font-variant: small-caps;
    letter-spacing: 0.5px;
    margin-top: 3px;
  }
  .detail-value { font-size: 15px; line-height: 1.2; }

  /* Back side */
  .card--back .back-logo {
    position: absolute;
    top: 70px;
    left: 0;
    right: 0;
  }
  .card--back .firm-name__letters { font-size: 96px; letter-spacing: 3px; }
  .card--back .firm-name__tagline { font-size: 20px; margin-top: 8px; }
  .office-cities {
    position: absolute;
    left: 0; right: 0; bottom: 24px;
    text-align: center;
    font-family: "Bitter", Georgia, serif;
    font-weight: 700;
    font-size: 20px;
    color: var(--paper-white);
  }
</style>
</head>
<body>
  <section class="card card--front" aria-label="Business card front">
    <header class="front-band">
      <div class="firm-name">
        <span class="firm-name__letters">KMR</span>
        <span class="firm-name__tagline">Personal Injury Attorneys</span>
      </div>
    </header>
    <div class="front-details">
      <p class="person-name">Tomas Velquist</p>
      <p class="person-title">Lawyer</p>
      <p class="detail-label">Address:</p>
      <p class="detail-value">712 W. Harlow Ave. 4th Floor<br>Brookvale, CA 90000.</p>
      <p class="detail-label">Phone:</p>
      <p class="detail-value">(555)014-2736 | (555)019-6521</p>
      <p class="detail-label">Email:</p>
      <p class="detail-value">Tomas@counselwestex.com</p>
    </div>
  </section>

  <section class="card card--back" aria-label="Business card back">
    <div class="firm-name back-logo">
      <span class="firm-name__letters">KMR</span>
      <span class="firm-name__tagline">Personal Injury Attorneys</span>
    </div>
    <p class="office-cities">Los Angeles - Santa Ana - San Diego - San Francisco</p>
  </section>
</body>
</html>
```